New lease of life for a tired Country Pub menu, QLD

I need to refresh my menus with updated prices. The menus need to be A4 (the menus are laminated and handed out over the bar. I'd like to include our logo. I will upload our existing menus as well as the new prices. The design should be humble yet stylish if that's ok, please

Target Market(s)

Locals, travellers and workers

Industry/Entity Type

Hospitality, Quintessential Country pub

Font styles to use
Sans Serif

Colors

Designer to choose colors to be used in the design.

Requirements
Must have
• as we run different menus on different nights
Nice to have
• our logo

```html
<!DOCTYPE html>
<html lang="en">
<head>
<meta charset="utf-8">
<title>Hotel Dunmore – Menu</title>
<link href="https://fonts.googleapis.com/css2?family=Montserrat:wght@400;600;700&display=swap" rel="stylesheet">
<style>
  :root{
    --page:#e9e9e9;
    --slate:#5a5a5a;
    --paper:#ffffff;
    --ink:#616161;
    --ribbon:#f4c35c;
    --ribbon-ink:#2b2b2b;
    --item:#f1f1f1;
    --leader:#bdbdbd;
    --photo-a:#343434;
    --photo-b:#1b1b1b;
  }
  *{margin:0;padding:0;box-sizing:border-box}
  html,body{width:1200px;height:1200px;overflow:hidden;background:var(--page)}
  body{font-family:"Montserrat",sans-serif}
  .menu{position:absolute;left:197px;top:30px;width:806px;height:1140px;background:var(--slate);overflow:hidden}
  .menu-shapes{position:absolute;inset:0;width:806px;height:1140px}
  .hero-photo{position:absolute;left:305px;top:-197px;width:556px;height:556px;border-radius:50%;
    background:radial-gradient(circle at 40% 60%,var(--photo-a),var(--photo-b))}
  .brand{position:absolute;left:60px;top:88px;width:230px;text-align:center;color:var(--ink);
    font-weight:600;font-size:38px;line-height:1.05;letter-spacing:.5px}
  .ribbon{position:absolute;background:var(--ribbon);color:var(--ribbon-ink);font-weight:700;
    font-size:15px;letter-spacing:.5px;display:flex;align-items:center;justify-content:center;
    clip-path:polygon(0 0,100% 14%,94% 55%,100% 100%,0 88%,5% 48%)}
  .ribbon-left{left:35px;width:171px}
  .ribbon-right{left:429px;width:220px}
  .menu-list{position:absolute;list-style:none;color:var(--item);font-size:12.6px}
  .menu-list li{display:flex;align-items:baseline;height:16.3px;line-height:16.3px;white-space:nowrap}
  .menu-list .name{flex:none}
  .menu-list .leader{flex:1;border-bottom:1px dotted var(--leader);margin:0 14px 4px 2px;min-width:8px}
  .menu-list .price{flex:none}
  .col-left{left:57px;width:286px}
  .col-right{left:462px;width:287px}
</style>
</head>
<body>
<div class="menu">
  <svg class="menu-shapes" viewBox="0 0 594 840" aria-hidden="true">
    <circle cx="160" cy="-10" r="255" fill="#ffffff"/>
    <rect x="0" y="0" width="594" height="60" fill="#ffffff"/>
  </svg>
  <div class="hero-photo" role="img" aria-label="Slices of prosciutto and rocket pizza on a dark stone board"></div>
  <svg class="menu-shapes" viewBox="0 0 594 840" aria-hidden="true">
    <path d="M0 250 Q60 268 111 280" fill="none" stroke="#ffffff" stroke-width="2"/>
    <path d="M296 230 Q430 300 594 258" fill="none" stroke="#ffffff" stroke-width="2.5"/>
    <path d="M215 195 L258 170" stroke="#6a6a6a" stroke-width="1.5"/>
    <circle cx="215" cy="195" r="11" fill="#6a6a6a"/>
    <circle cx="296" cy="230" r="11" fill="#ffffff" stroke="#5a5a5a" stroke-width="2"/>
    <circle cx="111" cy="280" r="13" fill="#ffffff"/>
  </svg>

  <div class="brand">HOTEL<br>DUNMORE</div>

  <div class="ribbon ribbon-left" style="top:417px;height:34px">DINNER MENU</div>
  <ul class="menu-list col-left" style="top:473px">
    <li><span class="name">Small bowl of Chips BBQ</span><span class="leader"></span><span class="price">$9.50</span></li>
    <li><span class="name">Large Bowl of Chips</span><span class="leader"></span><span class="price">$12.50</span></li>
    <li><span class="name">Garlic Bread</span><span class="leader"></span><span class="price">$10.50</span></li>
    <li><span class="name">Cheesy Sweet Chili Garlic Bread</span><span class="leader"></span><span class="price">$12.50</span></li>
    <li><span class="name">Cheesy Garlic Bread</span><span class="leader"></span><span class="price">$12.00</span></li>
    <li><span class="name">Loaded Garlic Bread</span><span class="leader"></span><span class="price">$15.50</span></li>
    <li><span class="name">T-Bone Steak</span><span class="leader"></span><span class="price">$41.99</span></li>
    <li><span class="name">Rump Steak</span><span class="leader"></span><span class="price">$40.99</span></li>
    <li><span class="name">Lambloin Chops</span><span class="leader"></span><span class="price">$35.00</span></li>
    <li><span class="name">Pork Chop (2)</span><span class="leader"></span><span class="price">$32.99</span></li>
    <li><span class="name">Pork Chop (1)</span><span class="leader"></span><span class="price">$29.00</span></li>
    <li><span class="name">Crumbed Chicken Thigh</span><span class="leader"></span><span class="price">$27.99</span></li>
    <li><span class="name">Crumbed Steak</span><span class="leader"></span><span class="price">$28.99</span></li>
    <li><span class="name">Chicken Parmi</span><span class="leader"></span><span class="price">$29.99</span></li>
    <li><span class="name">Beef Parmi</span><span class="leader"></span><span class="price">$30.99</span></li>
    <li><span class="name">Bangers and Mash</span><span class="leader"></span><span class="price">$23.00</span></li>
    <li><span class="name">Rissoles and Mash</span><span class="leader"></span><span class="price">$23.00</span></li>
    <li><span class="name">Lamb Rosemary Filo</span><span class="leader"></span><span class="price">$24.99</span></li>
    <li><span class="name">Roasted Veggie Scroll</span><span class="leader"></span><span class="price">$24.99</span></li>
    <li><span class="name">Chicken and Mushroom Filo</span><span class="leader"></span><span class="price">$24.99</span></li>
    <li><span class="name">Beer Battered Flathead (Main)</span><span class="leader"></span><span class="price">$27.99</span></li>
    <li><span class="name">Barramundi Panko</span><span class="leader"></span><span class="price">$27.99</span></li>
    <li><span class="name">Calamari Panko Crumbed</span><span class="leader"></span><span class="price">$27.99</span></li>
    <li><span class="name">Seafood Basket</span><span class="leader"></span><span class="price">$27.99</span></li>
    <li><span class="name">Lambshank and Mash</span><span class="leader"></span><span class="price">$32.00</span></li>
    <li><span class="name">Beer Battered Flathead (Kids)</span><span class="leader"></span><span class="price">$11.99</span></li>
    <li><span class="name">Nuggets and Chips</span><span class="leader"></span><span class="price">$11.99</span></li>
    <li><span class="name">Hawaiian Pizza with Chips (Kids)</span><span class="leader"></span><span class="price">$11.99</span></li>
    <li><span class="name">Calamari and Chips (Kids)</span><span class="leader"></span><span class="price">$11.99</span></li>
    <li><span class="name">Diane Sauce</span><span class="leader"></span><span class="price">$3.00</span></li>
    <li><span class="name">Gravy</span><span class="leader"></span><span class="price">$3.00</span></li>
    <li><span class="name">Mushroom Sauce</span><span class="leader"></span><span class="price">$3.00</span></li>
    <li><span class="name">Pepper Sauce</span><span class="leader"></span><span class="price">$3.00</span></li>
    <li><span class="name">Aioli</span><span class="leader"></span><span class="price">$1.50</span></li>
    <li><span class="name">Mayonnaise</span><span class="leader"></span><span class="price">$1.50</span></li>
    <li><span class="name">Tartare Sauce</span><span class="leader"></span><span class="price">$1.00</span></li>
    <li><span class="name">Mash</span><span class="leader"></span><span class="price">$4.99</span></li>
    <li><span class="name">Side of Salad</span><span class="leader"></span><span class="price">$10.00</span></li>
  </ul>

  <div class="ribbon ribbon-right" style="top:408px;height:41px">PIZZA MENU</div>
  <ul class="menu-list col-right" style="top:459px">
    <li><span class="name">BBQ Sweet Chili Chicken Pizza</span><span class="leader"></span><span class="price">$24.50</span></li>
    <li><span class="name">Hawaiian Pizza</span><span class="leader"></span><span class="price">$24.50</span></li>
    <li><span class="name">Meatlovers Pizza</span><span class="leader"></span><span class="price">$25.99</span></li>
    <li><span class="name">Pepperoni Pizza</span><span class="leader"></span><span class="price">$24.50</span></li>
    <li><span class="name">Supreme Pizza</span><span class="leader"></span><span class="price">$25.99</span></li>
    <li><span class="name">Tandoori Pizza</span><span class="leader"></span><span class="price">$24.50</span></li>
    <li><span class="name">Veggie Pizza</span><span class="leader"></span><span class="price">$24.50</span></li>
  </ul>

  <div class="ribbon ribbon-right" style="top:590px;height:43px">LUNCH MENU</div>
  <ul class="menu-list col-right" style="top:643px">
    <li><span class="name">Chicken Burger and Chips</span><span class="leader"></span><span class="price">$19.99</span></li>
    <li><span class="name">Beef Burger and Chips</span><span class="leader"></span><span class="price">$19.99</span></li>
    <li><span class="name">Steak Burger and Chips</span><span class="leader"></span><span class="price">$21.00</span></li>
    <li><span class="name">Barramundi Burger and Chips</span><span class="leader"></span><span class="price">$18.99</span></li>
    <li><span class="name">Caesar Salad</span><span class="leader"></span><span class="price">$17.99</span></li>
    <li><span class="name">Caesar Salad with Chicken</span><span class="leader"></span><span class="price">$21.00</span></li>
    <li><span class="name">Caesar Salad with Calamari</span><span class="leader"></span><span class="price">$22.50</span></li>
    <li><span class="name">Chicken Caesar Wrap</span><span class="leader"></span><span class="price">$19.00</span></li>
    <li><span class="name">Honey Mustard Salad with Chicken</span><span class="leader"></span><span class="price">$19.00</span></li>
    <li><span class="name">Bangin Burrito</span><span class="leader"></span><span class="price">$21.00</span></li>
  </ul>

  <div class="ribbon ribbon-right" style="top:817px;height:42px">BEEF PARMIS</div>
  <ul class="menu-list col-right" style="top:867px">
    <li><span class="name">Beef Parmi</span><span class="leader"></span><span class="price">$30.00</span></li>
    <li><span class="name">Aussie Beef Parmigiana</span><span class="leader"></span><span class="price">$30.95</span></li>
    <li><span class="name">Beef Hawaiian Parmi</span><span class="leader"></span><span class="price">$30.95</span></li>
    <li><span class="name">Beef Hot and Spicy Parmi</span><span class="leader"></span><span class="price">$30.95</span></li>
    <li><span class="name">Beef Meatlovers Parmi</span><span class="leader"></span><span class="price">$30.95</span></li>
  </ul>

  <div class="ribbon ribbon-right" style="top:954px;height:49px;font-size:17px">CHICKEN PARMIS</div>
  <ul class="menu-list col-right" style="top:1011px">
    <li><span class="name">Chicken Parmi</span><span class="leader"></span><span class="price">$29.99</span></li>
    <li><span class="name">Aussie Chicken Parmi</span><span class="leader"></span><span class="price">$30.95</span></li>
    <li><span class="name">Chicken Hawaiian Parmi</span><span class="leader"></span><span class="price">$30.95</span></li>
    <li><span class="name">Chicken Meatlovers Parmi</span><span class="leader"></span><span class="price">$30.95</span></li>
    <li><span class="name">Chicken Hot and Spicy Parmi</span><span class="leader"></span><span class="price">$30.95</span></li>
  </ul>
</div>
</body>
</html>
```